"Sun On Water" Gospel Presentation Booklet

I need a design for a 12 page (including front/back cover) square booklet, with religious images and aesthetically pleasing fonts/designs. I want it to be very simple, and very straightforward. The main focus of the project is it's content. So the design should be very nice, but also should point to the content, not take away from it, or create distraction. People should be more focused on the words than the imagery.

I enjoy modern designs, I need a sharp aesthetic that is clean and neat. Nothing over the top.
I have attached a word document with the content I would like on the pages.

Colors
0592cd
0255a3
33a6d7
85cae6
85acd3
3276b5
9bcb3b
f04a50
f68d4c

Requirements
Should not have
• Super feminine colors/aesthetics

```html
<!DOCTYPE html>
<html lang="en">
<head>
<meta charset="utf-8">
<title>Sun On Water – Booklet Pages</title>
<link rel="stylesheet" href="https://fonts.googleapis.com/css2?family=Montserrat:wght@400;700&family=Open+Sans:wght@400&display=swap">
<style>
  :root{
    --paper:#ffffff;
    --ink:#000000;
    --sky-deep:#0255a3;
    --sky-mid:#0592cd;
    --sky-light:#33a6d7;
    --sky-pale:#85cae6;
    --sky-soft:#85acd3;
    --sky-steel:#3276b5;
    --cloud:#e9f2fa;
    --navy:#1a2a5c;
    --type-white:#ffffff;
    --type-faded:rgba(190,212,240,0.6);
  }
  *{margin:0;padding:0;box-sizing:border-box}
  html,body{width:1200px;height:1200px;overflow:hidden;background:var(--paper)}
  .board{position:relative;width:1200px;height:1200px;font-family:"Montserrat",sans-serif}

  .page-label{position:absolute;font-family:"Open Sans",sans-serif;font-size:44px;line-height:1;color:var(--ink)}
  .page-label--fp{left:264px;top:338px}
  .page-label--p1{left:389px;top:1145px}
  .page-label--p2{left:776px;top:1150px}

  /* Front page */
  .cover{position:absolute;left:394px;top:91px;width:419px;height:497px}
  .cover__art{position:absolute;inset:0;
    background:
      radial-gradient(ellipse 60% 55% at 50% 72%,rgba(50,118,181,.95) 0%,rgba(133,172,211,.85) 45%,rgba(233,242,250,0) 100%),
      radial-gradient(ellipse 30% 60% at 55% 30%,rgba(51,166,215,.8) 0%,rgba(133,202,230,.4) 60%,rgba(255,255,255,0) 100%),
      linear-gradient(to bottom,rgba(255,255,255,1) 0%,rgba(255,255,255,0) 55%),
      linear-gradient(to bottom,var(--cloud) 0%,var(--sky-soft) 100%)}
  .cover__title{position:absolute;left:0;width:100%;text-align:center;font-weight:700;line-height:1}
  .cover__title--main{top:260px;font-size:50px;letter-spacing:14px;padding-left:14px;
    background:linear-gradient(90deg,#cfe3f4 0%,#9cc3e6 45%,var(--sky-deep) 100%);
    -webkit-background-clip:text;background-clip:text;color:transparent}
  .cover__title--sub{top:345px;font-size:17px;letter-spacing:12px;padding-left:12px;color:var(--type-white)}

  /* Pages 1 and 2 */
  .spread{position:absolute;left:265px;top:641px;width:677px;height:487px;overflow:hidden}
  .spread__sky{position:absolute;inset:0;
    background:
      radial-gradient(circle at 63% 34%,#ffffff 0,#ffffff 2%,rgba(255,255,255,.55) 7%,rgba(255,255,255,0) 20%),
      radial-gradient(ellipse 80% 22% at 50% 100%,rgba(240,246,252,.95) 0%,rgba(233,242,250,.7) 50%,rgba(233,242,250,0) 100%),
      linear-gradient(150deg,rgba(255,255,255,0) 30%,rgba(240,246,252,.7) 44%,rgba(255,255,255,0) 58%),
      linear-gradient(120deg,var(--navy) 0%,var(--sky-deep) 28%,var(--sky-mid) 60%,var(--sky-light) 80%,var(--sky-deep) 100%)}
  .spread__fold{position:absolute;left:339px;top:0;width:1px;height:100%;background:rgba(255,255,255,.12)}

  .word-cross{position:absolute;inset:0;font-weight:700;line-height:1}
  .word-cross__letter{position:absolute;font-size:62px;color:var(--type-faded)}
  .word-cross__letter--top{left:149px;top:137px}
  .word-cross__letter--bottom{left:156px;top:290px}
  .word-cross__main{position:absolute;left:82px;top:214px;font-size:64px;letter-spacing:7px;color:var(--type-white)}

  .verse{position:absolute;left:454px;width:124px;font-weight:400;
    font-size:11px;line-height:13.6px;color:var(--type-white);letter-spacing:.3px}
  .verse--lead{top:191px}
  .verse--body{top:245px}
  .ornament{position:absolute;left:457px;top:225px;width:104px;height:14px}
</style>
</head>
<body>
<main class="board">

  <span class="page-label page-label--fp">FP</span>

  <section class="cover" aria-label="Front page">
    <div class="cover__art" role="img" aria-label="Photo of an open white door standing in a blue sky, with clouds spilling out below it"></div>
    <div class="cover__title cover__title--main">SUN</div>
    <div class="cover__title cover__title--sub">ON WATER</div>
  </section>

  <section class="spread" aria-label="Pages 1 and 2">
    <div class="spread__sky" role="img" aria-label="Photo of a bright blue sky with the sun shining through a band of white clouds"></div>
    <div class="spread__fold"></div>
    <div class="word-cross">
      <span class="word-cross__letter word-cross__letter--top">G</span>
      <span class="word-cross__main">GOD</span>
      <span class="word-cross__letter word-cross__letter--bottom">D</span>
    </div>
    <p class="verse verse--lead">He is holy, that means He's perfect.</p>
    <div class="ornament" role="img" aria-label="Small white crown of thorns ornament" style="background:linear-gradient(to bottom,rgba(255,255,255,0) 20%,rgba(255,255,255,.7) 45%,rgba(255,255,255,.7) 55%,rgba(255,255,255,0) 80%)"></div>
    <p class="verse verse--body">In fact, He is so perfect, corruption cannot live with Him.</p>
  </section>

  <span class="page-label page-label--p1">P1</span>
  <span class="page-label page-label--p2">P2</span>

</main>
</body>
</html>
```